Infographic for small business and social media

We are looking for a long term infographics designer to work with, and what a better way to start then with a competition? We want small business relation and social media related inforgraphics done on a fortnightly basis (rates will be re-negotiated for a longer term regular contract). We are looking for someone that can:

Turn content into a visually appealing and easy to understand infographic
Someone with a interesting and funky style (even thought we are about business, we want to have a more innovative image, which is not completely corporate)

Here is the first article to turn into an infographic:

http://www.tradepathhubnet.com.au/2013/07/25/social-media-offers-revenue-gains-to-small-business-latest-zelk-statistics/

```html
<!DOCTYPE html>
<html lang="en">
<head>
<meta charset="utf-8">
<title>Social Media Benefits – Zelk statistics</title>
<link rel="stylesheet" href="https://fonts.googleapis.com/css2?family=Oswald:wght@500;700&family=Archivo+Narrow:wght@400;500&display=swap">
<style>
  :root {
    --cream: #f2efd6;
    --banner: #f5d327;
    --banner-fold: #d9b818;
    --ink: #231f20;
    --grey: #5a5a5a;
    --green: #9bd13f;
    --green-light: #c9ea7a;
    --brown: #6b4a2b;
    --pie-main: #cfac22;
    --pie-slice: #f4d52c;
    --callora: #2bb6e8;
    --linkwell: #1f74b4;
    --friendlo: #3b5998;
    --blog: #7cc242;
    --chirpo: #4fc4ea;
  }
  * { box-sizing: border-box; margin: 0; padding: 0; }
  html, body { width: 1200px; height: 879px; overflow: hidden; background: var(--cream); }
  body { font-family: "Archivo Narrow", "Arial Narrow", sans-serif; color: var(--ink); }
  .canvas { position: relative; width: 1200px; height: 879px; background: var(--cream); }
  .abs { position: absolute; }

  .banner { left: 0; top: 0; width: 1200px; height: 112px; }
  .title { left: 0; width: 1200px; top: 10px; text-align: center; font-family: "Oswald", sans-serif; font-weight: 700; font-size: 62px; letter-spacing: 1px; }
  .subtitle { left: 0; width: 1200px; top: 126px; text-align: center; font-size: 27px; color: var(--grey); }

  .dots-h { height: 0; border-top: 4px dotted var(--ink); }
  .dots-v { width: 0; border-left: 4px dotted var(--ink); }

  .stat-num { font-family: "Oswald", sans-serif; font-weight: 700; font-size: 30px; line-height: 1; }
  .stat-text { font-size: 16px; line-height: 1.2; }
  .usage-20 { left: 122px; top: 226px; width: 186px; }
  .usage-20 .stat-num { float: left; margin-right: 6px; font-size: 28px; }
  .usage-19 { left: 120px; top: 344px; width: 180px; }
  .usage-19 .stat-num { float: left; margin-right: 6px; font-size: 24px; }

  .network { top: 236px; width: 74px; text-align: center; }
  .network .mark { display: block; width: 44px; height: 44px; margin: 0 auto 6px; border-radius: 8px; }
  .network .name { font-size: 14px; font-weight: 500; display: block; height: 20px; white-space: nowrap; }
  .network .share { font-family: "Oswald", sans-serif; font-weight: 500; font-size: 27px; display: block; margin-top: 8px; }

  .section-title { font-family: "Oswald", sans-serif; font-weight: 700; font-size: 36px; }
  .col-title { font-family: "Oswald", sans-serif; font-weight: 500; font-size: 18px; text-decoration: underline; text-underline-offset: 4px; }

  .pie { width: 140px; height: 140px; }
  .pie-label { width: 160px; font-size: 14px; line-height: 1.2; }
  .pie-label .stat-num { font-size: 32px; letter-spacing: -1px; float: left; margin-right: 4px; }

  .web-bar { left: 737px; top: 240px; width: 422px; height: 26px; border: 3px solid var(--ink); border-radius: 14px; background: var(--green-light); overflow: hidden; }
  .web-bar .fill { width: 38%; height: 100%; background: var(--green); }
  .web-share { left: 800px; top: 206px; font-family: "Oswald", sans-serif; font-weight: 700; font-size: 26px; line-height: 1; }
  .web-caption { left: 737px; width: 422px; top: 268px; text-align: center; font-family: "Oswald", sans-serif; font-weight: 700; font-size: 35px; }

  .benefit { left: 745px; width: 404px; height: 68px; border: 7px solid var(--brown); outline: 2px solid var(--cream); outline-offset: -11px; display: flex; align-items: center; padding-left: 12px; }
  .benefit .stat-num { font-size: 38px; width: 100px; letter-spacing: -1px; }
  .benefit .stat-text { font-size: 17px; flex: 1; text-align: center; padding-right: 18px; }
</style>
</head>
<body>
<main class="canvas">
  <svg class="abs banner" viewBox="0 0 1200 112" aria-hidden="true">
    <polygon points="200,18 262,18 262,96 200,96 226,57" fill="var(--banner-fold)"/>
    <polygon points="1000,18 938,18 938,96 1000,96 974,57" fill="var(--banner-fold)"/>
    <rect x="240" y="0" width="720" height="100" fill="var(--banner)"/>
  </svg>
  <h1 class="abs title">SOCIAL MEDIA BENEFITS</h1>
  <p class="abs subtitle">To small and medium business (SMEs): Zelk statistics</p>

  <div class="abs dots-h" style="left:0;top:190px;width:722px"></div>
  <div class="abs dots-h" style="left:737px;top:190px;width:463px"></div>

  <svg class="abs" style="left:30px;top:240px" width="96" height="128" viewBox="0 0 96 128" aria-hidden="true">
    <circle cx="47" cy="47" r="40" fill="none" stroke="var(--green-light)" stroke-width="12"/>
    <path d="M47 7 A40 40 0 0 1 85 34.6" fill="none" stroke="var(--green)" stroke-width="12"/>
    <polyline points="47,93 47,118 96,118" fill="none" stroke="var(--ink)" stroke-width="1.5" stroke-dasharray="4 3"/>
  </svg>
  <div class="abs usage-20"><span class="stat-num">20%</span><span class="stat-text">Of SMEs surveyed were using social media for business purposes</span></div>
  <div class="abs usage-19"><span class="stat-num">19%</span><span class="stat-text">Used it to make free business phone calls</span></div>

  <div class="abs dots-v" style="left:320px;top:214px;height:172px"></div>

  <div class="abs network" style="left:346px"><span class="mark" style="background:var(--callora);border-radius:50%"></span><span class="name">Callora</span><span class="share">19%</span></div>
  <div class="abs network" style="left:414px"><span class="mark" style="background:var(--linkwell)"></span><span class="name">Linkwell</span><span class="share">18%</span></div>
  <div class="abs network" style="left:480px"><span class="mark" style="background:var(--friendlo)"></span><span class="name">Friendlo</span><span class="share">16%</span></div>
  <div class="abs network" style="left:546px"><span class="mark" style="background:var(--blog)"></span><span class="name">company blog</span><span class="share">9%</span></div>
  <div class="abs network" style="left:614px"><span class="mark" style="background:var(--chirpo)"></span><span class="name">Chirpo</span><span class="share">6%</span></div>

  <div class="abs dots-h" style="left:0;top:416px;width:722px"></div>
  <h2 class="abs section-title" style="left:198px;top:420px">COMPARISON OF SMEs</h2>
  <div class="abs dots-h" style="left:0;top:476px;width:722px"></div>

  <h3 class="abs col-title" style="left:106px;top:496px">USING SOCIAL MEDIA</h3>
  <h3 class="abs col-title" style="left:430px;top:496px">ALL SMEs</h3>
  <div class="abs dots-v" style="left:364px;top:500px;height:340px"></div>

  <svg class="abs pie" style="left:63px;top:537px" viewBox="-70 -70 140 140" aria-hidden="true">
    <circle r="64" fill="var(--pie-main)" stroke="var(--ink)" stroke-width="3"/>
    <path d="M0 0 L0 -64 A64 64 0 0 1 62.9 12 Z" fill="var(--pie-slice)" stroke="var(--ink)" stroke-width="3"/>
  </svg>
  <div class="abs pie-label" style="left:200px;top:560px"><span class="stat-num">28%</span>Reported an increase in revenue</div>

  <svg class="abs pie" style="left:63px;top:697px" viewBox="-70 -70 140 140" aria-hidden="true">
    <circle r="64" fill="var(--pie-main)" stroke="var(--ink)" stroke-width="3"/>
    <path d="M0 0 L0 -64 A64 64 0 0 1 57.9 -27.3 Z" fill="var(--pie-slice)" stroke="var(--ink)" stroke-width="3"/>
  </svg>
  <div class="abs pie-label" style="left:200px;top:716px"><span class="stat-num">18%</span>Were less likely to report a fall in revenue</div>

  <svg class="abs pie" style="left:397px;top:537px" viewBox="-70 -70 140 140" aria-hidden="true">
    <circle r="64" fill="var(--pie-main)" stroke="var(--ink)" stroke-width="3"/>
    <path d="M0 0 L0 -64 A64 64 0 0 1 62.9 12 Z" fill="var(--pie-slice)" stroke="var(--ink)" stroke-width="3"/>
  </svg>
  <div class="abs pie-label" style="left:530px;top:560px"><span class="stat-num">18%</span>Reported an increase in revenue. A difference of 10%</div>

  <svg class="abs pie" style="left:397px;top:697px" viewBox="-70 -70 140 140" aria-hidden="true">
    <circle r="64" fill="var(--pie-main)" stroke="var(--ink)" stroke-width="3"/>
    <path d="M0 0 L0 -64 A64 64 0 0 1 40.8 49.3 Z" fill="var(--pie-slice)" stroke="var(--ink)" stroke-width="3"/>
  </svg>
  <div class="abs pie-label" style="left:530px;top:716px"><span class="stat-num">39%</span>Were less likely to report a fall in revenue</div>

  <div class="abs web-share">38%</div>
  <div class="abs web-bar"><div class="fill"></div></div>
  <div class="abs web-caption">of the SMEs have a website</div>

  <div class="abs benefit" style="top:320px"><span class="stat-num">45%</span><span class="stat-text">Increased costumer leads</span></div>
  <div class="abs benefit" style="top:400px"><span class="stat-num">37%</span><span class="stat-text">Better conversion rate for sales leads</span></div>
  <div class="abs benefit" style="top:483px"><span class="stat-num">42%</span><span class="stat-text">Said that their website made them more competitive</span></div>
  <div class="abs benefit" style="top:565px"><span class="stat-num">12%</span><span class="stat-text">Sell products and services online directly to customers</span></div>
  <div class="abs benefit" style="top:648px"><span class="stat-num">11%</span><span class="stat-text">Accept online payments with a shopping cart</span></div>
  <div class="abs benefit" style="top:733px"><span class="stat-num">9%</span><span class="stat-text">Allow payments trhough a mobile app</span></div>
</main>
</body>
</html>
```